Copper lark buildworks

Copper lark buildworks is a small construction company.
Who is a licenced builder, Carpenter, joiner,
working on heritage ,new build, speacial projects and sometimes furniture

Industry/Entity Type

Construction

```html
<!DOCTYPE html>
<html lang="en">
<head>
<meta charset="utf-8">
<title>Copper lark buildworks – Business Card</title>
<link rel="stylesheet" href="https://fonts.googleapis.com/css2?family=Nunito:wght@800&family=Open+Sans:ital,wght@0,400;1,300&family=Roboto:wght@300;400&display=swap">
<style>
  :root {
    --page-bg: #ecebe8;
    --card-black: #231f20;
    --card-green: #136b3c;
    --ink-white: #ffffff;
  }
  * { box-sizing: border-box; margin: 0; padding: 0; }
  html, body { width: 1200px; height: 1200px; overflow: hidden; }
  body { background: var(--page-bg); position: relative; }

  .business-card {
    position: absolute;
    left: 100px; top: 320px;
    width: 1000px; height: 560px;
    background: var(--card-green);
    box-shadow: 0 10px 30px rgba(0,0,0,0.18);
    overflow: hidden;
    color: var(--ink-white);
  }
  .brand-panel {
    position: absolute; left: 0; top: 0;
    width: 340px; height: 100%;
    background: var(--card-black);
  }
  .brand-name {
    position: absolute; left: 0; top: 152px; width: 340px;
    text-align: center;
    font-family: "Roboto", sans-serif; font-weight: 400;
    font-size: 62px; line-height: 82px;
  }
  .edge-tab {
    position: absolute; right: 0; top: 32px;
    width: 64px; height: 495px;
    background: var(--card-black);
    border-radius: 48px 0 0 48px;
  }
  .owner-name {
    position: absolute; left: 355px; top: 36px; width: 545px;
    text-align: center;
    font-family: "Nunito", sans-serif; font-weight: 800;
    font-size: 70px; letter-spacing: 1px; line-height: 80px;
  }
  .owner-role {
    position: absolute; left: 600px; top: 108px; width: 293px;
    text-align: right;
    font-family: "Open Sans", sans-serif; font-style: italic; font-weight: 300;
    font-size: 38px; letter-spacing: 1px;
  }
  .phone {
    position: absolute; left: 470px; top: 180px;
    display: flex; align-items: center; gap: 26px;
    font-family: "Roboto", sans-serif; font-weight: 300;
    font-size: 54px; letter-spacing: 2px;
  }
  .phone svg { width: 34px; height: 52px; }
  .services-title {
    position: absolute; left: 382px; top: 282px;
    font-family: "Open Sans", sans-serif; font-size: 22px;
  }
  .services-list {
    position: absolute; top: 330px; list-style: none;
    font-family: "Open Sans", sans-serif; font-size: 22px;
  }
  .services-list li { height: 52px; }
  .services-list--main { left: 378px; }
  .services-list--extra { left: 684px; }
</style>
</head>
<body>
  <article class="business-card">
    <div class="brand-panel">
      <p class="brand-name">Copper<br>lark<br>buildworks</p>
    </div>
    <div class="edge-tab"></div>

    <h1 class="owner-name">Miles Harrow</h1>
    <p class="owner-role">Owner</p>

    <p class="phone">
      <svg viewBox="0 0 34 52" fill="none" stroke="#ffffff" stroke-width="2.5">
        <rect x="3" y="2" width="28" height="48" rx="5"/>
        <line x1="3" y1="10" x2="31" y2="10"/>
        <line x1="3" y1="40" x2="31" y2="40"/>
        <line x1="13" y1="6" x2="21" y2="6"/>
        <circle cx="17" cy="45" r="2"/>
      </svg>
      <span>0400555127</span>
    </p>

    <p class="services-title">Services</p>
    <ul class="services-list services-list--main">
      <li>- Licensed builder</li>
      <li>- Carpenter</li>
      <li>- Joiner</li>
      <li>- New Build</li>
    </ul>
    <ul class="services-list services-list--extra">
      <li>- Special Projects</li>
      <li>- Furniture</li>
      <li>- Working On Heritage</li>
    </ul>
  </article>
</body>
</html>
```